Tarn Studio PPT design

We are looking for a fresh and funky PPT design that is both eye-catching and allows room/whitespace for us to get the content across. We are a social media agency based in China and our logo although simple sort of reflects the nature of the company. There are two main tasks for this PPT, one as a business card to show-case our case-studies, but also as a back-drop to our pitch presentations and other client presentations. These presentations are a mix of visuals, text and graphs. The key message we want to get across is that we are professional, creative and fresh. We think that using our four support colours may work but are open to suggestions.
Current website www.tarnasia-example.com
Reason: Hi All,
as we have just guaranteed the payment we extended the deadline to allow for more submissions. Please bear with us.
Thanks,
Tarn Studio Team
Reason: To see more designs, we extend the deadline to March 18, 2014. Thanks.
Target Market(s)
Marketing CMO's, company CEO's, product managers, social media managers
Industry/Entity Type
Business

```html
<!DOCTYPE html>
<html lang="en">
<head>
<meta charset="utf-8">
<title>Tarn Studio – Slide 2</title>
<link href="https://fonts.googleapis.com/css2?family=Michroma&display=swap" rel="stylesheet">
<style>
  :root {
    --ink: #111111;
    --orange: #f15a29;
    --magenta: #e6007e;
    --purple: #7b2a8f;
    --green: #8cc63f;
    --rule: #a6a6a6;
    --paper: #ffffff;
  }
  * { margin: 0; padding: 0; box-sizing: border-box; }
  html, body { width: 1200px; height: 900px; overflow: hidden; background: var(--paper); }
  .slide {
    position: relative;
    width: 1200px;
    height: 900px;
    font-family: "Michroma", sans-serif;
    color: var(--ink);
  }
  .slide-title {
    position: absolute;
    left: 32px;
    top: 26px;
    font-size: 37px;
    font-weight: 400;
    letter-spacing: 4px;
    line-height: 1;
    white-space: nowrap;
  }
  .slide-title .accent { color: var(--orange); }
  .title-rule {
    position: absolute;
    left: 30px;
    top: 74px;
    width: 648px;
    height: 2px;
    background: var(--rule);
  }
  .corner-accent {
    position: absolute;
    right: 42px;
    top: 0;
    width: 72px;
    height: 72px;
    background: linear-gradient(90deg, var(--green), var(--purple), var(--magenta), var(--orange));
  }
  .content {
    position: absolute;
    left: 38px;
    top: 146px;
    display: grid;
    grid-template-columns: 615px 540px;
    row-gap: 34px;
  }
  .section-heading {
    color: var(--magenta);
    font-size: 24px;
    font-weight: 400;
    letter-spacing: 4px;
    line-height: 34px;
    white-space: nowrap;
  }
  .section-body {
    font-size: 17.5px;
    line-height: 36px;
    letter-spacing: 3px;
    word-spacing: 3px;
    white-space: nowrap;
  }
  .section-body .line { display: block; }
  .footer-rule {
    position: absolute;
    left: 0;
    top: 813px;
    width: 1200px;
    height: 3px;
    background: var(--rule);
  }
  .brand {
    position: absolute;
    left: 20px;
    top: 836px;
    display: flex;
    align-items: center;
    gap: 12px;
    font-size: 30px;
    line-height: 1;
    color: var(--ink);
  }
  .brand-mark { width: 14px; height: 14px; background: var(--magenta); }
  .page-marker {
    position: absolute;
    right: 0;
    top: 834px;
    display: flex;
    gap: 7px;
    height: 42px;
  }
  .page-accent {
    width: 26px;
    height: 42px;
    background: linear-gradient(90deg, var(--purple), var(--magenta), var(--orange));
  }
  .page-number {
    width: 72px;
    height: 42px;
    background: var(--ink);
    color: var(--paper);
    font-size: 28px;
    line-height: 42px;
    text-align: center;
  }
</style>
</head>
<body>
<main class="slide">
  <h1 class="slide-title">PROJECT <span class="accent">TITLE HERE</span></h1>
  <div class="title-rule"></div>
  <div class="corner-accent" role="img" aria-label="Decorative colour accent in green, purple, magenta and orange"></div>

  <section class="content">
    <article class="section">
      <h2 class="section-heading">Lorem ipsum dolor sit</h2>
      <p class="section-body">
        <span class="line">Lorem ipsum dolor sit Lorem ipsum</span>
        <span class="line">dolor sit Lorem ipsum dolor sit</span>
        <span class="line">Lorem ipsum dolor sit Lorem ipsum</span>
        <span class="line">dolor sit Lorem ipsum dolor sit</span>
        <span class="line">Lorem ipsum dolor sit Lorem ipsum</span>
        <span class="line">dolor sit Lorem ipsum dolor sit</span>
      </p>
    </article>
    <article class="section">
      <h2 class="section-heading">Lorem ipsum dolor sit</h2>
      <p class="section-body">
        <span class="line">Lorem ipsum dolor sit Lorem ipsum</span>
        <span class="line">dolor sit Lorem ipsum dolor sit</span>
        <span class="line">Lorem ipsum dolor sit Lorem ipsum</span>
        <span class="line">dolor sit Lorem ipsum dolor sit</span>
        <span class="line">Lorem ipsum dolor sit Lorem ipsum</span>
        <span class="line">dolor sit Lorem ipsum</span>
      </p>
    </article>
    <article class="section">
      <h2 class="section-heading">Lorem ipsum dolor sit</h2>
      <p class="section-body">
        <span class="line">Lorem ipsum dolor sit Lorem ipsum</span>
        <span class="line">dolor sit Lorem ipsum dolor sit</span>
        <span class="line">Lorem ipsum dolor sit Lorem ipsum</span>
        <span class="line">dolor sit Lorem ipsum dolor sit</span>
        <span class="line">Lorem ipsum dolor sit Lorem ipsum</span>
        <span class="line">dolor sit Lorem ipsum dolor sit</span>
        <span class="line">Lorem ipsum dolor sit Lorem ipsum</span>
        <span class="line">dolor sit Lorem ipsum</span>
      </p>
    </article>
    <article class="section">
      <h2 class="section-heading">Lorem ipsum dolor sit</h2>
      <p class="section-body">
        <span class="line">Lorem ipsum dolor sit Lorem ipsum</span>
        <span class="line">dolor sit Lorem ipsum dolor sit</span>
        <span class="line">Lorem ipsum dolor sit Lorem ipsum</span>
        <span class="line">dolor sit Lorem ipsum dolor sit</span>
        <span class="line">Lorem ipsum dolor sit Lorem ipsum</span>
        <span class="line">dolor sit Lorem ipsum dolor sit</span>
        <span class="line">Lorem ipsum dolor sit Lorem ipsum</span>
        <span class="line">dolor sit Lorem ipsum</span>
      </p>
    </article>
  </section>

  <div class="footer-rule"></div>

  <div class="brand">
    <span class="brand-mark"></span>
    <span class="brand-name">Tarn Studio</span>
  </div>

  <div class="page-marker">
    <div class="page-accent" role="img" aria-label="Decorative colour accent in purple, magenta and orange"></div>
    <div class="page-number">2</div>
  </div>
</main>
</body>
</html>
```